Company Business cards ZOR. Modern professional look

We need a new business card design using the new logo you created for us. Make it modern and professional. It has to be simple yet innovative. We are a recruitment and IT Services provider and we are publicly listed so the card has to be of the highest standard and interesting to look at.

Make sure the card is simple but crisp.

Target Market(s)

Clients

Industry/Entity Type

Recruitment

Contact Information for Business Card

Name
Position Title
Company Name
Address
Phone email fax website

Font styles to use
Other font styles liked:
• Calibri

Requirements
Must have
• Modern and professional
Nice to have
• Clean, simple yet interesting
Should not have
• Old style, boring

```html
<!DOCTYPE html>
<html lang="en">
<head>
<meta charset="utf-8">
<title>ZOR Business Card</title>
<link href="https://fonts.googleapis.com/css2?family=Lato:wght@400;700;900&display=swap" rel="stylesheet">
<style>
  :root {
    --brand-red: #e8181f;
    --ink: #1d1d1f;
    --paper: #ffffff;
    --band-grey: #e4e5e6;
    --stage: #eef0f0;
  }
  * { margin: 0; padding: 0; box-sizing: border-box; }
  html, body {
    width: 1200px; height: 900px; overflow: hidden;
    background: var(--stage);
    font-family: "Lato", sans-serif;
  }
  .canvas {
    position: relative; width: 1200px; height: 900px;
  }
  .card {
    position: absolute; left: 340px; width: 520px; height: 300px;
    box-shadow: 0 10px 26px rgba(0,0,0,0.12);
    overflow: hidden;
  }
  .card-front { top: 100px; background: var(--brand-red); }
  .card-back  { top: 500px; background: var(--paper); }

  .front-mark {
    position: absolute; inset: 0;
    display: flex; align-items: center; justify-content: center; gap: 14px;
  }
  .front-mark .dot {
    width: 18px; height: 18px; border-radius: 50%; background: var(--paper);
  }
  .front-mark .name {
    color: var(--paper); font-weight: 900; font-size: 64px; letter-spacing: 2px;
  }

  .back-band { position: absolute; inset: 0; }

  .back-mark {
    position: absolute; top: 34px; right: 120px;
    display: flex; align-items: center; gap: 8px;
  }
  .back-mark .dot {
    width: 11px; height: 11px; border-radius: 50%; background: var(--brand-red);
  }
  .back-mark .name {
    color: var(--ink); font-weight: 900; font-size: 34px; letter-spacing: 1px;
  }

  .holder { position: absolute; left: 40px; top: 96px; color: var(--ink); }
  .holder-name { font-size: 25px; font-weight: 400; line-height: 1.1; }
  .holder-title { font-size: 14px; margin-top: 2px; }

  .contact-list {
    position: absolute; left: 40px; top: 162px;
    list-style: none; color: var(--ink); font-size: 13px; line-height: 19px;
  }
  .contact-list .label {
    display: inline-block; width: 14px; color: var(--brand-red); font-weight: 700;
  }
  .contact-list .sep { margin-right: 6px; }
  .contact-list .address { margin-top: 2px; }
</style>
</head>
<body>
<main class="canvas">

  <section class="card card-front" aria-label="Business card front">
    <div class="front-mark">
      <span class="dot"></span>
      <span class="name">ZOR</span>
    </div>
  </section>

  <section class="card card-back" aria-label="Business card back">
    <svg class="back-band" width="520" height="300" viewBox="0 0 520 300" aria-hidden="true">
      <path d="M430 0 Q520 140 460 300 L520 300 L520 0 Z" fill="var(--band-grey)"/>
    </svg>

    <div class="back-mark">
      <span class="dot"></span>
      <span class="name">ZOR</span>
    </div>

    <div class="holder">
      <p class="holder-name">Marcus Delane</p>
      <p class="holder-title">President</p>
    </div>

    <ul class="contact-list">
      <li><span class="label">E</span><span class="sep">:</span>info@zorgroup.com</li>
      <li><span class="label">T</span><span class="sep">:</span>310 555 0142</li>
      <li><span class="label">F</span><span class="sep">:</span>310 555 0142</li>
      <li><span class="label">W</span><span class="sep">:</span>zorgroup.com</li>
      <li class="address">48 Harbour Lane, Crest Road</li>
      <li>Province 40217</li>
    </ul>
  </section>

</main>
</body>
</html>
```